flayer design

I need app advertisement, to use it in flayers,
I have 2 messages and you can use any of them, (just use one of them)
Key notes:
• The flayers is for university student,
• The a flayers should be eye catching colors
• Don’t sue teacher picture or student or people wearing eye classes
• Size of the flayer should be quarter of an A4 paper,
• The design should be simple and nicely looking
• You should add zelkor and mubrevo (available in the dock shelf) logo
Note: After accepting the flayer, I will provide you Arabic text, since the flayer should be in Arabic, and I am providing the English for you now so you can understand and play with text easily,
Note: I will not wait until eth end I will choose the first bets design I have,
Note: attached app logo
Thanks

```html
<!DOCTYPE html>
<html lang="en">
<head>
<meta charset="utf-8">
<title>Talimo App – Private Tutor Flyer</title>
<link rel="stylesheet" href="https://fonts.googleapis.com/css2?family=Oswald:wght@300;400&family=Raleway:wght@200;800;900&display=swap">
<style>
  :root {
    --paper: #ffffff;
    --orange-light: #ffb400;
    --orange-mid: #f9a11b;
    --orange-deep: #f1701c;
    --ink: #111111;
    --red: #ec1c24;
    --white: #ffffff;
    --badge-dark: #6d6e71;
    --badge-green: #8dc63f;
    --wood-light: #e9a54b;
    --wood-dark: #b96a22;
  }
  html, body {
    margin: 0;
    padding: 0;
    width: 847px;
    height: 1200px;
    overflow: hidden;
    background: var(--paper);
  }
  .flyer {
    position: relative;
    width: 847px;
    height: 1200px;
    display: block;
  }
  .headline {
    font-family: "Oswald", sans-serif;
    font-weight: 400;
    fill: var(--ink);
  }
  .offer-light {
    font-family: "Raleway", sans-serif;
    font-weight: 200;
    fill: var(--white);
  }
  .offer-bold {
    font-family: "Raleway", sans-serif;
    font-weight: 900;
    fill: var(--white);
  }
  .offer-number {
    font-family: "Raleway", sans-serif;
    font-weight: 900;
    fill: var(--red);
    font-variant-numeric: lining-nums;
    font-feature-settings: "lnum" 1, "onum" 0;
  }
  .app-name {
    font-family: "Raleway", sans-serif;
    font-weight: 800;
    fill: var(--red);
  }
  .badge-small,
  .badge-large {
    font-family: "Raleway", sans-serif;
    font-weight: 800;
    fill: var(--white);
  }
</style>
</head>
<body>
<svg class="flyer" width="847" height="1200" viewBox="0 0 847 1200" xmlns="http://www.w3.org/2000/svg">
  <defs>
    <radialGradient id="bg-glow" cx="0.7" cy="0.2" r="1">
      <stop offset="0" stop-color="var(--orange-light)"/>
      <stop offset="0.55" stop-color="var(--orange-mid)"/>
      <stop offset="1" stop-color="var(--orange-deep)"/>
    </radialGradient>
    <radialGradient id="flourish-tone" cx="0.4" cy="0.5" r="0.6">
      <stop offset="0" stop-color="#ec1c24" stop-opacity="0.55"/>
      <stop offset="1" stop-color="#ec1c24" stop-opacity="0"/>
    </radialGradient>
    <linearGradient id="wood-tone" x1="0" y1="0" x2="1" y2="1">
      <stop offset="0" stop-color="var(--wood-light)"/>
      <stop offset="1" stop-color="var(--wood-dark)"/>
    </linearGradient>
  </defs>

  <rect class="background" x="0" y="0" width="836" height="1186" fill="url(#bg-glow)"/>

  <line class="rule-vertical" x1="45" y1="0" x2="45" y2="1186" stroke="#5a2a00" stroke-width="1.5"/>
  <line class="rule-horizontal" x1="0" y1="404" x2="587" y2="404" stroke="#ffe7a8" stroke-width="1.5"/>

  <rect class="flourish" role="img" aria-label="Red floral swirl ornament rising from the left edge" x="0" y="280" width="360" height="440" rx="180" fill="url(#flourish-tone)"/>

  <text class="headline" x="85" y="198" font-size="182" textLength="568" lengthAdjust="spacingAndGlyphs">DO YOU NEED</text>
  <text class="headline" x="85" y="362" font-size="174" textLength="707" lengthAdjust="spacingAndGlyphs">PRIVATE TUTOR ?</text>

  <text class="offer-light" x="434" y="495" font-size="84" textLength="353" lengthAdjust="spacingAndGlyphs">WE HAVE</text>
  <text class="offer-bold" x="322" y="573" font-size="76" textLength="462" lengthAdjust="spacingAndGlyphs">MORE THAN</text>
  <text class="offer-number" x="399" y="766" font-size="232" textLength="391" lengthAdjust="spacingAndGlyphs">900</text>
  <text class="app-name" x="418" y="829" font-size="44" textLength="372" lengthAdjust="spacingAndGlyphs">TALIMO APP</text>

  <g class="store-badge store-badge--zelkor">
    <rect x="79" y="986" width="201" height="73" rx="10" fill="var(--white)"/>
    <rect x="85" y="992" width="189" height="61" rx="7" fill="var(--badge-dark)"/>
    <rect x="96" y="1008" width="22" height="30" rx="3" fill="none" stroke="var(--white)" stroke-width="3"/>
    <text class="badge-small" x="128" y="1012" font-size="10">Available on the zelkor</text>
    <text class="badge-large" x="128" y="1042" font-size="26" textLength="138" lengthAdjust="spacingAndGlyphs">Dock Shelf</text>
  </g>
  <g class="store-badge store-badge--mubrevo">
    <rect x="79" y="1076" width="201" height="73" rx="10" fill="var(--white)"/>
    <rect x="85" y="1082" width="189" height="61" rx="7" fill="var(--badge-green)"/>
    <rect x="96" y="1098" width="26" height="26" rx="4" fill="var(--white)"/>
    <text class="badge-small" x="130" y="1102" font-size="10">Available on the mubrevo</text>
    <text class="badge-large" x="130" y="1132" font-size="26" textLength="136" lengthAdjust="spacingAndGlyphs">Dock Shelf</text>
  </g>

  <rect class="profile-card" role="img" aria-label="Illustration of an open tutor profile booklet with a five-star rating on a wooden board" x="314" y="861" width="482" height="297" rx="18" fill="url(#wood-tone)"/>
</svg>
</body>
</html>
```